Epoxy coatings company needs a logo/business card design.

My company name is "Lustrous Resin Works", and I am looking for a company logo and business card design.
My initial thought was to use "Æ"in 'Lu'strous, and would also like to see ideas on how to play around with the fact that the first 3 letters (Lrw) are also the acronym of the company name.
I specialize in garage floor and interior epoxy coatings, paint flake broadcasts, quartz broadcasts, and solid color epoxy floors, concrete repairs.
I like images I've seen of a silhouetted person running a floor grinder. It keeps the design of the card simple. I'm not necessarily opposed to using images of the floors on the card, but I'd prefer to keep the front simple (Company name, my name, phone number, email) and maybe put pictures on the back. I've included a few of my personal pictures of floors I've done (including a before, after, and when the garage was being used after)
My colors are darker green (Fern/Forest/Hunter, etc), and Bronze.

Contact Information for Business Card

Name: Dana Kellworth Email: lustrousresinworks@mailbrook.net Phone: (555)318-9042 Instagram: lustrous_resin_works

Colors

Designer to choose colors to be used in the design.

Requirements
Nice to have
• I've included a business card designed for someone else, that contains the silhouette that I'm looking for. The floor grinder that I use is large like the one pictured (Torvex G40R).

```html
<!DOCTYPE html>
<html lang="en">
<head>
<meta charset="utf-8">
<title>Lustrous Resin Works – Business Card</title>
<link href="https://fonts.googleapis.com/css2?family=Montserrat:wght@400;500;700;800&display=swap" rel="stylesheet">
<style>
  :root {
    --bg: #2a2a2a;
    --green: #4e7a3f;
    --green-light: #7fa85f;
    --ink: #1a1a1a;
    --white: #ffffff;
    --stone-a: #5b5550;
    --stone-b: #3c3936;
  }
  * { box-sizing: border-box; margin: 0; padding: 0; }
  html, body { width: 1200px; height: 1186px; overflow: hidden; }
  body {
    background: var(--bg);
    font-family: "Montserrat", sans-serif;
    position: relative;
  }
  .card {
    position: absolute;
    left: 150px;
    width: 900px;
    height: 514px;
    border-radius: 28px;
    overflow: hidden;
  }
  .card--back { top: 60px; }
  .card--front { top: 612px; background: var(--white); }

  /* back side */
  .stone-texture {
    position: absolute; inset: 0;
    background: radial-gradient(ellipse at 40% 30%, var(--stone-a), var(--stone-b));
  }
  .brand-mark {
    position: absolute;
    display: flex; align-items: center; gap: 16px;
    color: var(--green-light);
    font-weight: 800;
    letter-spacing: 1px;
    white-space: nowrap;
  }
  .card--back .brand-mark { left: 50%; top: 50%; transform: translate(-50%, -50%); font-size: 52px; }
  .brand-dot { border-radius: 50%; background: currentColor; flex: none; }
  .card--back .brand-dot { width: 46px; height: 46px; }

  /* front side */
  .card--front .brand-mark { left: 60px; top: 160px; font-size: 29px; color: var(--green); letter-spacing: 0.5px; }
  .card--front .brand-dot { width: 28px; height: 28px; }
  .divider-line {
    position: absolute; left: 0; right: 0; top: 288px;
    height: 5px; background: var(--ink);
  }
  .green-band {
    position: absolute; left: 0; right: 0; top: 302px; bottom: 0;
    background: var(--green);
  }
  .person-name {
    position: absolute; right: 60px; top: 40px; text-align: right;
  }
  .person-name h1 { color: var(--green); font-size: 30px; font-weight: 800; }
  .person-name p { font-size: 15px; color: var(--ink); margin-top: 2px; }
  .grinder-silhouette {
    position: absolute; right: 50px; top: 118px; width: 290px; height: 396px;
    background: linear-gradient(180deg, #1f1f1f, #0d0d0d);
    border-radius: 40px 40px 6px 6px;
  }
  .contact-block {
    position: absolute; left: 60px; top: 330px; color: var(--white);
  }
  .contact-block h2 { font-size: 22px; font-weight: 700; }
  .contact-block .region { font-size: 18px; font-weight: 400; margin-bottom: 16px; }
  .contact-list { list-style: none; }
  .contact-list li { display: flex; align-items: center; gap: 14px; font-size: 18px; margin-bottom: 8px; }
  .contact-list svg { width: 16px; height: 16px; fill: var(--white); flex: none; }
</style>
</head>
<body>

<section class="card card--back">
  <div class="stone-texture" role="img" aria-label="Photo of a flake-broadcast epoxy floor surface"></div>
  <div class="brand-mark"><span class="brand-dot"></span>Lustrous Resin Works</div>
</section>

<section class="card card--front">
  <div class="brand-mark"><span class="brand-dot"></span>Lustrous Resin Works</div>
  <div class="person-name">
    <h1>Dana Kellworth</h1>
    <p>President</p>
  </div>
  <div class="divider-line"></div>
  <div class="green-band"></div>
  <div class="grinder-silhouette" role="img" aria-label="Silhouette of a worker pushing a floor grinder"></div>
  <div class="contact-block">
    <h2>Lustrous Resin Works</h2>
    <p class="region">Southern California, USA</p>
    <ul class="contact-list">
      <li><svg viewBox="0 0 16 16"><path d="M3 1l3 3-1.5 2a9 9 0 0 0 5.5 5.5L12 10l3 3-2 2C7 15 1 9 1 3z"/></svg>+1 555-318-9042</li>
      <li><svg viewBox="0 0 16 16"><path d="M1 3h14v10H1z M1 3l7 6 7-6" stroke="#4e7a3f" stroke-width="1.2"/></svg>info@mailbrook.net</li>
      <li><svg viewBox="0 0 16 16"><circle cx="8" cy="8" r="7"/></svg>www.lustrousresin.net</li>
    </ul>
  </div>
</section>

</body>
</html>
```